Web Design for Cedarfield Yard Crew

Cedarfield Yard Crew needs the photoshop files for a simple, clean and professional web design. I need a home and subpage design, although they can be very similar. See pagestridelab.com for a desired layout, although I'd like to see more design than shown on that site. The goal of the site is to attract both lawn maintenance/landscape customers and build a partner network of consultants that serve the US market. The following are needed:

- home and subpage design
- page: Home, Services, Locations, Consultants, FAQ, Contact
- if subpages have header photo, need to include 5 different header photos for each page
- favicon
Updates

I'll award the design based on the homepage concept. The minor subpage changes and other elements can be worked out in the workroom stage. Thanks, Reid

Industry/Entity Type

It Professional

```html
<!DOCTYPE html>
<html lang="en">
<head>
<meta charset="utf-8">
<title>Cedarfield Yard Crew</title>
<link href="https://fonts.googleapis.com/css2?family=PT+Sans:wght@400;700&family=PT+Sans+Narrow:wght@400;700&family=Roboto+Condensed:wght@400;700&display=swap" rel="stylesheet">
<style>
:root{
  --green:#6aa84a;
  --green-light:#8fc160;
  --green-dark:#5b9a3c;
  --text:#777;
  --text-dark:#222;
  --line:#dcdcdc;
  --bg:#f0f0f0;
  --nav-top:#5a5b5e;
  --nav-bottom:#3a3b3e;
  --white:#fff;
}
*{box-sizing:border-box;margin:0;padding:0}
html,body{width:1024px;height:1200px;overflow:hidden}
body{position:relative;background:var(--bg);font-family:"PT Sans",sans-serif;color:var(--text)}
.site-header{position:absolute;left:0;top:0;width:1024px;height:82px;background:var(--white)}
.brand{position:absolute;left:45px;top:15px;display:flex;align-items:center;gap:12px}
.brand-mark{width:50px;height:50px;border:4px solid #555;border-radius:6px}
.brand-name{font-family:"PT Sans",sans-serif;font-size:28px;font-weight:400;color:#555;line-height:1}
.contact-block{position:absolute;top:18px;padding-left:15px;border-left:1px solid #ddd}
.contact-block.email{left:605px}
.contact-block.phone{left:822px}
.contact-title{font-family:"Roboto Condensed",sans-serif;font-size:19px;font-weight:700;color:var(--green);line-height:22px}
.contact-line{display:flex;align-items:center;gap:6px;font-family:"PT Sans Narrow",sans-serif;font-size:14px;color:#555;margin-top:3px}
.main-nav{position:absolute;left:0;top:82px;width:1024px;height:38px;background:linear-gradient(var(--nav-top),var(--nav-bottom))}
.main-nav a{position:absolute;top:0;height:38px;line-height:40px;font-family:"Roboto Condensed",sans-serif;font-weight:700;font-size:14px;color:var(--white);text-decoration:none;transform:translateX(-50%)}
.main-nav a.active{left:101px;width:113px;text-align:center;background:#66676a;border-top:3px solid var(--green);line-height:37px}
.hero{position:absolute;left:0;top:120px;width:1024px;height:204px;background:linear-gradient(180deg,#5f9a2e 0%,#7cc23a 55%,#8fd04a 100%)}
.hero-band{position:absolute;left:0;top:324px;width:1024px;height:38px;background:linear-gradient(#6a6b6e,#3b3c3f)}
.content-card{position:absolute;left:46px;top:388px;width:614px;height:614px;background:var(--white);border:1px solid #d8d8d8;padding:24px 21px}
.page-title{font-family:"PT Sans Narrow",sans-serif;font-size:19px;font-weight:400;color:var(--green);margin-bottom:14px}
.lead{font-size:11.5px;font-weight:700;line-height:20px;color:#777;margin-bottom:12px}
.body-copy{font-size:10.5px;line-height:16px;color:#888}
.section-head{display:flex;align-items:center;gap:10px;margin:24px 0 0 2px;width:535px}
.section-head h3{font-size:12px;font-weight:700;color:#888}
.section-head span{flex:1;height:4px;border-top:1px solid var(--line);border-bottom:1px solid var(--line)}
.ticks{list-style:none;margin-top:14px;margin-left:3px}
.ticks li{display:flex;align-items:center;gap:12px;font-size:10.5px;color:#888;height:27px}
.accordion{margin-top:18px;margin-left:3px}
.acc-item{display:flex;gap:15px;margin-bottom:23px}
.acc-toggle{flex:none;width:16px;height:16px;background:#333;color:#fff;font-size:11px;line-height:16px;text-align:center}
.acc-toggle.open{background:var(--green-light)}
.acc-q{font-size:10.5px;color:var(--text-dark);line-height:16px}
.acc-a{font-size:10.5px;line-height:16px;color:#888;margin-top:8px;width:500px}
.form-card{position:absolute;left:684px;top:388px;width:296px;height:348px;background:var(--white);border:1px solid #d8d8d8}
.form-head{height:64px;background:linear-gradient(var(--green-light),var(--green-dark));color:#fff;font-family:"PT Sans Narrow",sans-serif;font-size:18px;letter-spacing:-0.3px;padding-left:22px;line-height:66px}
.form-body{padding:13px 22px 0 23px}
.field{display:block;width:251px;height:28px;border:1px solid #ddd;margin-bottom:7px;font-size:10.5px;color:#888;padding:7px 9px}
.field-row{display:flex;justify-content:space-between;width:251px}
.field-row .field{width:118px}
.field.message{height:55px}
.submit{display:inline-block;margin-top:13px;margin-left:-5px;height:30px;padding:0 15px;border:1px solid #ccc;border-radius:15px;background:linear-gradient(#fff,#e6e6e6);font-family:"Roboto Condensed",sans-serif;font-weight:700;font-size:10.5px;color:#555;line-height:29px;box-shadow:0 1px 2px rgba(0,0,0,.2)}
.site-footer{position:absolute;left:0;top:1020px;width:1024px;height:140px;background:var(--white)}
.site-footer .brand{top:42px}
.footer-nav{position:absolute;left:686px;top:36px}
.footer-nav h4{font-size:11px;font-weight:400;color:#555;letter-spacing:.3px}
.footer-links{display:grid;grid-template-columns:105px 104px 80px;row-gap:8px;margin-top:10px;list-style:none}
.footer-links li{font-size:11px;color:#777;padding-left:12px;position:relative}
.footer-links li::before{content:"";position:absolute;left:1px;top:4px;border-left:4px solid #888;border-top:3px solid transparent;border-bottom:3px solid transparent}
.bottom-bar{position:absolute;left:0;top:1160px;width:1024px;height:40px;background:var(--green);color:#fff;font-size:11px;display:flex;justify-content:space-between;align-items:center;padding:0 45px 0 46px}
</style>
</head>
<body>
<header class="site-header">
  <div class="brand"><span class="brand-mark"></span><span class="brand-name">Cedarfield Yard Crew</span></div>
  <div class="contact-block email">
    <div class="contact-title">EMAIL US</div>
    <div class="contact-line">
      <svg width="15" height="11" viewBox="0 0 15 11"><rect x=".5" y=".5" width="14" height="10" fill="none" stroke="#aaa"/><path d="M.5 .5 7.5 6 14.5 .5" fill="none" stroke="#aaa"/></svg>
      info@cedarfieldyardcrew.com
    </div>
  </div>
  <div class="contact-block phone">
    <div class="contact-title">CALL US TODAY</div>
    <div class="contact-line">
      <svg width="13" height="13" viewBox="0 0 13 13"><path d="M3 1 5 4 4 5.5C5 7.5 6 8.5 7.5 9L9 8l3 2-1 2C6 12 1 7 1 2z" fill="none" stroke="#aaa"/></svg>
      +1800 55 7272
    </div>
  </div>
</header>

<nav class="main-nav">
  <a class="active" href="#">HOME</a>
  <a href="#" style="left:250px">SERVICES</a>
  <a href="#" style="left:406px">LOCATIONS</a>
  <a href="#" style="left:575px">CONSULTANTS</a>
  <a href="#" style="left:725px">FAQ</a>
  <a href="#" style="left:850px">CONTACT US</a>
</nav>

<div class="hero" role="img" aria-label="Photo of a mown green lawn bordered by pink and red flower beds"></div>
<div class="hero-band"></div>

<main class="content-card">
  <h1 class="page-title">Headline/Title</h1>
  <p class="lead">It is a long established fact that a reader will be distracted by the readable content of a page when looking at its layout.</p>
  <p class="body-copy">The point of using Lorem Ipsum is that it has a more-or-less normal distribution of letters, as opposed to using 'Content here, content here', making it look like readable English. Many desktop publishing packages and web page editors now use Lorem Ipsum as their default model text, and a search for 'lorem ipsum' will uncover many web sites still in their infancy. Various versions have evolved over the years, sometimes by accident, sometimes on purpose (injected humour and the like).</p>

  <div class="section-head"><h3>Headline</h3><span></span></div>
  <ul class="ticks">
    <li><svg width="15" height="15" viewBox="0 0 15 15"><circle cx="7.5" cy="7.5" r="7.5" fill="#8fc160"/><path d="M6.5 4.5 9.5 7.5 6.5 10.5" fill="none" stroke="#fff" stroke-width="1.6"/></svg>Cras rutrum leo at odio volutpat id blandit fugiats ipsum ornare.</li>
    <li><svg width="15" height="15" viewBox="0 0 15 15"><circle cx="7.5" cy="7.5" r="7.5" fill="#8fc160"/><path d="M6.5 4.5 9.5 7.5 6.5 10.5" fill="none" stroke="#fff" stroke-width="1.6"/></svg>Donec fermentum porttitor nunc, sit amet gravida est porttitor vel.</li>
    <li><svg width="15" height="15" viewBox="0 0 15 15"><circle cx="7.5" cy="7.5" r="7.5" fill="#8fc160"/><path d="M6.5 4.5 9.5 7.5 6.5 10.5" fill="none" stroke="#fff" stroke-width="1.6"/></svg>Maecenas quis nisi in uctus adipiscing sed vehicula tellus amet</li>
    <li><svg width="15" height="15" viewBox="0 0 15 15"><circle cx="7.5" cy="7.5" r="7.5" fill="#8fc160"/><path d="M6.5 4.5 9.5 7.5 6.5 10.5" fill="none" stroke="#fff" stroke-width="1.6"/></svg>dolore.</li>
  </ul>

  <div class="section-head" style="margin-top:30px"><h3>Headline</h3><span></span></div>
  <div class="accordion">
    <div class="acc-item"><span class="acc-toggle">+</span><p class="acc-q">In hac habitasse platea dictumst. Duis vel neque vitae magna scelerisque volutpat.</p></div>
    <div class="acc-item"><span class="acc-toggle">+</span><p class="acc-q">Suspendisse condimentum varius orci nec volutpat. Praesent eu felis est, ac feugiat ledui odios.</p></div>
    <div class="acc-item"><span class="acc-toggle open">&minus;</span>
      <div><p class="acc-q">Aliquam eu ligula viverra tortor rutrum vestibulum sit amet in orci dolores amets unsers.</p>
      <p class="acc-a">Ut tristique turpis sed nibh auctor at interdum est rutrum. Suspendisse condimentum varius orci nec volutpat. Praesent eu felis est, ac feugiat leo. In sit amet dui odio, eget facilisis nunc. Sed eros nunc, porttitor vitae euismod ut, lacinia id urna. Suspendisse id diam id nisi facilisis faucibus ac interdum lorem.</p></div>
    </div>
  </div>
</main>

<aside class="form-card">
  <h2 class="form-head">Learn More About Becoming A Consultant</h2>
  <div class="form-body">
    <div class="field">Name (required)</div>
    <div class="field">Email (required)</div>
    <div class="field">Phone</div>
    <div class="field-row"><div class="field">City</div><div class="field">State</div></div>
    <div class="field message">Message</div>
    <span class="submit">SUBMIT FORM</span>
  </div>
</aside>

<footer class="site-footer">
  <div class="brand"><span class="brand-mark"></span><span class="brand-name">Cedarfield Yard Crew</span></div>
  <nav class="footer-nav">
    <h4>NAVIGATION</h4>
    <ul class="footer-links">
      <li>Home</li><li>Locations</li><li>FAQ</li>
      <li>Services</li><li>Consultants</li><li>Contact</li>
    </ul>
  </nav>
</footer>
<div class="bottom-bar"><span>Copyright © 2014 - Cedarfield Yard Crew</span><span>Sitemap | Privacy Policy</span></div>
</body>
</html>
```